PHD-project

i need the figures to be in the same stile. info is inside the file. There are 5 figures that need redesign. this is for PhD.

Target Market(s)

it will be used in my phd

Colors

Designer to choose colors to be used in the design.

```html
<!DOCTYPE html>
<html lang="en">
<head>
<meta charset="utf-8">
<title>PhD Figures – Design Thinking Research</title>
<link rel="stylesheet" href="https://fonts.googleapis.com/css2?family=Roboto:wght@300;400;700;900&display=swap">
<style>
  :root {
    --teal: #7fcad4;
    --teal-light: #b2e0e6;
    --teal-dark: #16807f;
    --blue: #5a98f8;
    --blue-light: #8fbcfa;
    --grey-line: #d9d9d9;
    --dot: #555a60;
    --ink: #2a2a2a;
    --navy-ink: #3a5571;
    --accent-red: #c6202e;
    --deep-red: #b5121f;
    --amber: #e9a52b;
    --amber-light: #f2bd49;
    --sky: #17a9ee;
    --outline: #1f4f9e;
    --paper: #ffffff;
  }
  html, body {
    margin: 0;
    padding: 0;
    width: 1200px;
    height: 1118px;
    overflow: hidden;
    background: var(--paper);
  }
  .figure-sheet {
    display: block;
    width: 1200px;
    height: 1118px;
    font-family: "Roboto", Arial, sans-serif;
  }
  .label-year { font-weight: 900; font-size: 19px; fill: var(--ink); text-anchor: middle; }
  .label-note { font-weight: 400; font-size: 12.5px; fill: var(--ink); }
  .venn-light { font-weight: 300; fill: #fff; text-anchor: middle; }
  .venn-dark { font-weight: 400; fill: var(--ink); text-anchor: middle; }
  .venn-accent { font-weight: 400; fill: var(--accent-red); text-anchor: middle; }
  .axis-label { font-weight: 900; font-size: 19px; fill: var(--navy-ink); text-anchor: middle; }
  .axis-label-light { font-weight: 300; font-size: 20px; fill: #555; }
  .reflect-head { font-weight: 900; fill: #fff; text-anchor: middle; }
  .reflect-list { font-weight: 300; fill: #fff; text-anchor: middle; }
  .reflect-node { font-weight: 900; text-anchor: middle; }
  .reflect-caption { font-weight: 400; fill: var(--ink); text-anchor: middle; }
  .dash { stroke: #8a8a8a; stroke-width: 1.2; stroke-dasharray: 5 4; fill: none; }
</style>
</head>
<body>
<svg class="figure-sheet" viewBox="0 0 1988 1852" xmlns="http://www.w3.org/2000/svg">
  <defs>
    <linearGradient id="grad-teal" x1="0" y1="0" x2="1" y2="1">
      <stop offset="0" stop-color="#7cc7d1"/>
      <stop offset="0.5" stop-color="#a9dde4"/>
      <stop offset="1" stop-color="#78c5d0"/>
    </linearGradient>
    <linearGradient id="grad-blue" x1="0" y1="0" x2="1" y2="1">
      <stop offset="0" stop-color="#5b97f7"/>
      <stop offset="0.5" stop-color="#8fbdfa"/>
      <stop offset="1" stop-color="#5b97f7"/>
    </linearGradient>
    <radialGradient id="grad-pearl" cx="0.45" cy="0.35" r="0.7">
      <stop offset="0" stop-color="#ffffff"/>
      <stop offset="0.7" stop-color="#ececec"/>
      <stop offset="1" stop-color="#d2d2d2"/>
    </radialGradient>
    <linearGradient id="grad-bubble-grey" x1="0" y1="0" x2="0" y2="1">
      <stop offset="0" stop-color="#f2f2f2"/>
      <stop offset="1" stop-color="#d6d6d6"/>
    </linearGradient>
    <linearGradient id="grad-amber" x1="0" y1="0" x2="1" y2="1">
      <stop offset="0" stop-color="#e9a22a"/>
      <stop offset="0.5" stop-color="#f2bd4a"/>
      <stop offset="1" stop-color="#e7a02a"/>
    </linearGradient>
    <linearGradient id="grad-red" x1="0" y1="0" x2="1" y2="1">
      <stop offset="0" stop-color="#b5121f"/>
      <stop offset="0.5" stop-color="#d2303a"/>
      <stop offset="1" stop-color="#b0101c"/>
    </linearGradient>
    <radialGradient id="grad-sky" cx="0.5" cy="0.4" r="0.7">
      <stop offset="0" stop-color="#7fd2fb"/>
      <stop offset="1" stop-color="#109fe9"/>
    </radialGradient>
    <clipPath id="clip-half-left"><path d="M259,1044 A168,168 0 0 1 595,1044 Z"/></clipPath>
    <clipPath id="clip-oval-left"><ellipse cx="1158" cy="944" rx="175" ry="158"/></clipPath>
    <clipPath id="clip-half-left-b"><path d="M250,1374 A154,154 0 0 1 558,1374 Z"/></clipPath>
    <clipPath id="clip-oval-left-b"><ellipse cx="957" cy="1334" rx="131" ry="123"/></clipPath>
  </defs>

  <!-- Research timeline -->
  <g class="timeline">
    <line x1="334" y1="505" x2="500" y2="505" stroke="url(#grad-teal)" stroke-width="11"/>
    <line x1="500" y1="505" x2="832" y2="505" stroke="var(--grey-line)" stroke-width="11"/>
    <line x1="832" y1="505" x2="1052" y2="505" stroke="url(#grad-blue)" stroke-width="11"/>

    <path class="dash" d="M267,342 V455 L331,478 V492"/>
    <path class="dash" d="M599,342 V455 L663,476 V492"/>
    <path class="dash" d="M500,517 V540 L428,568 V715"/>
    <path class="dash" d="M836,517 V540 L765,568 V715"/>
    <path class="dash" d="M1052,517 V537 L980,563 V707"/>

    <text class="label-note"><tspan x="273" y="388">PREQUEL WITH</tspan><tspan x="273" y="403">STUDENT-LED</tspan><tspan x="273" y="418">INNOVATION</tspan></text>
    <text class="label-note" x="604" y="388">INTERVENTIONS</text>
    <text class="label-note"><tspan x="434" y="634">FIRST ROUND OF</tspan><tspan x="434" y="649">INTERVIEWS</tspan></text>
    <text class="label-note"><tspan x="771" y="635">SECOND ROUND OF</tspan><tspan x="771" y="650">INTERVIEWS</tspan></text>
    <text class="label-note"><tspan x="986" y="630">SECOND ROUND OF</tspan><tspan x="986" y="645">INTERVIEWS</tspan></text>

    <!-- 2013 -->
    <g class="milestone">
      <path d="M471,450 H471 L500,476 L529,450 Z" fill="#d8d8d8"/>
      <rect x="421" y="252" width="158" height="198" rx="52" fill="url(#grad-bubble-grey)"/>
      <circle cx="500" cy="332" r="68" fill="#f4f4f4" role="img" aria-label="Icon: presenter with one participant"/>
      <text class="label-year" x="501" y="434">2013</text>
    </g>
    <!-- 2015 -->
    <g class="milestone">
      <path d="M803,448 L832,474 L861,448 Z" fill="#d8d8d8"/>
      <rect x="752" y="250" width="159" height="198" rx="52" fill="url(#grad-bubble-grey)"/>
      <circle cx="831" cy="330" r="68" fill="#f4f4f4" role="img" aria-label="Icon: presenter with a group of participants"/>
      <text class="label-year" x="830" y="428">2015</text>
    </g>
    <!-- 2017 -->
    <g class="milestone">
      <path d="M1023,449 L1052,476 L1081,449 Z" fill="#6ba3f8"/>
      <rect x="972" y="251" width="159" height="198" rx="52" fill="url(#grad-blue)"/>
      <circle cx="1052" cy="331" r="68" fill="#f4f4f4" role="img" aria-label="Icon: signed document"/>
      <text class="label-year" x="1056" y="433">2017</text>
    </g>
    <!-- 2012 -->
    <g class="milestone">
      <path d="M302,566 L331,539 L360,566 Z" fill="#86cbd5"/>
      <rect x="252" y="565" width="159" height="198" rx="52" fill="url(#grad-teal)"/>
      <circle cx="331" cy="684" r="68" fill="#f4f4f4" role="img" aria-label="Icon: idea bulb with gears"/>
      <text class="label-year" x="330" y="601">2012</text>
    </g>
    <!-- 2013-2015 -->
    <g class="milestone">
      <path d="M636,568 L665,542 L694,568 Z" fill="#e8e8e8"/>
      <rect x="587" y="567" width="159" height="198" rx="52" fill="url(#grad-bubble-grey)"/>
      <circle cx="666" cy="686" r="68" fill="#f4f4f4" role="img" aria-label="Icon: group of three people"/>
      <text class="label-year" x="669" y="601">2013-2015</text>
    </g>

    <circle cx="334" cy="503" r="11" fill="var(--dot)"/>
    <circle cx="500" cy="503" r="11" fill="var(--dot)"/>
    <circle cx="832" cy="503" r="11" fill="var(--dot)"/>
    <circle cx="1052" cy="503" r="11" fill="var(--dot)"/>
  </g>

  <!-- Reflection model (teal) -->
  <g class="reflection reflection--teal">
    <circle cx="1474" cy="372" r="145" fill="url(#grad-teal)"/>
    <text class="reflect-head" font-size="18"><tspan x="1476" y="317">REFLECTION INVOLVES</tspan><tspan x="1476" y="338">THREE ELEMENTS:</tspan></text>
    <text class="reflect-list" font-size="18"><tspan x="1476" y="381">RETURNING TO EXPERIENCE</tspan><tspan x="1476" y="402">ATTENDING TO FEELINGS</tspan><tspan x="1476" y="424">EVALUATING EXPERIENCE</tspan></text>
    <circle cx="1350" cy="548" r="82" fill="url(#grad-pearl)"/>
    <circle cx="1598" cy="544" r="82" fill="url(#grad-pearl)"/>
    <text class="reflect-node" font-size="19" fill="var(--teal-dark)"><tspan x="1344" y="546">REFLECTING</tspan><tspan x="1344" y="568">ON ACTION</tspan></text>
    <text class="reflect-node" font-size="19" fill="var(--teal-dark)"><tspan x="1598" y="544">REFLECTING</tspan><tspan x="1598" y="566">ON ACTION</tspan></text>
    <text class="reflect-caption" font-size="17"><tspan x="1476" y="664">REFLECTION IS AN ACTIVE PROCESS OF</tspan><tspan x="1476" y="685">WITNESSING ONE'S WON EXPERIENCE IN ORDER TO</tspan><tspan x="1476" y="707">EXAMINE IT MORE CLOSELY, GIVE MEANING TO IT,</tspan><tspan x="1476" y="728">AND LEARN FROM IT.</tspan></text>
  </g>

  <!-- Design thinking half-Venn (teal/blue) -->
  <g class="half-venn half-venn--cool">
    <path d="M259,1044 A168,168 0 0 1 595,1044 Z" fill="url(#grad-teal)"/>
    <path d="M426,1044 A168,168 0 0 1 762,1044 Z" fill="url(#grad-blue)"/>
    <path d="M426,1044 A168,168 0 0 1 762,1044 Z" fill="url(#grad-pearl)" clip-path="url(#clip-half-left)"/>
    <text class="venn-light" font-size="18"><tspan x="361" y="968">ANALYTHIC</tspan><tspan x="361" y="991">THINKING</tspan></text>
    <text class="venn-accent" font-size="18"><tspan x="505" y="974">DESIGN</tspan><tspan x="505" y="996">THINKING</tspan></text>
    <text class="venn-light" font-size="18"><tspan x="656" y="938">INTUITIVE</tspan><tspan x="656" y="961">AND</tspan><tspan x="656" y="983">CREATIVE</tspan><tspan x="656" y="1006">THINKING</tspan></text>
    <text class="axis-label"><tspan x="340" y="1077">UNDERSTAND</tspan><tspan x="340" y="1103">PROBLEM</tspan></text>
    <text class="axis-label"><tspan x="677" y="1071">DESIGN</tspan><tspan x="677" y="1097">SOLUTION</tspan></text>
    <path d="M495,1069 H538 V1063 L555,1076 L538,1089 V1083 H495 Z" fill="#fff" stroke="#2c5f9e" stroke-width="2.5"/>
    <path d="M526,1092 H483 V1086 L466,1100 L483,1113 V1107 H526 Z" fill="#fff" stroke="#2c5f9e" stroke-width="2.5"/>
  </g>

  <!-- Contribution Venn (teal/blue) -->
  <g class="venn venn--cool">
    <ellipse cx="1158" cy="944" rx="175" ry="158" fill="url(#grad-teal)"/>
    <ellipse cx="1376" cy="947" rx="173" ry="158" fill="url(#grad-blue)"/>
    <ellipse cx="1376" cy="947" rx="173" ry="158" fill="url(#grad-pearl)" clip-path="url(#clip-oval-left)"/>
    <text class="venn-dark" font-size="17"><tspan x="1095" y="923">DESIGN THINKING IN</tspan><tspan x="1095" y="953">MANAGEMENT AND</tspan><tspan x="1095" y="983">BUSINESS STRATEGY</tspan></text>
    <text class="venn-accent" font-size="17"><tspan x="1264" y="944">CONTRIBUTION</tspan><tspan x="1264" y="974">AREA</tspan></text>
    <text class="venn-dark" font-size="17"><tspan x="1440" y="940">RESEARCH THROUGH</tspan><tspan x="1440" y="970">DESIGN - R&amp;D</tspan></text>
  </g>

  <!-- Design thinking half-Venn (warm) -->
  <g class="half-venn half-venn--warm">
    <path d="M250,1374 A154,154 0 0 1 558,1374 Z" fill="url(#grad-amber)"/>
    <path d="M395,1374 A154,154 0 0 1 703,1374 Z" fill="url(#grad-red)"/>
    <path d="M395,1374 A154,154 0 0 1 703,1374 Z" fill="url(#grad-sky)" clip-path="url(#clip-half-left-b)"/>
    <path d="M250,1374 A154,154 0 0 1 404,1220" fill="none" stroke="var(--outline)" stroke-width="3"/>
    <path d="M395,1374 A154,154 0 0 1 703,1374" fill="none" stroke="var(--outline)" stroke-width="3"/>
    <path d="M250,1374 A154,154 0 0 1 558,1374" fill="none" stroke="var(--outline)" stroke-width="1" stroke-dasharray="3 3" clip-path="url(#clip-half-left-b)"/>
    <line x1="249" y1="1374" x2="704" y2="1374" stroke="var(--outline)" stroke-width="3"/>
    <text class="venn-light" font-size="17"><tspan x="343" y="1305">ANALYTHIC</tspan><tspan x="343" y="1325">THINKING</tspan></text>
    <text class="venn-light" font-size="17"><tspan x="472" y="1310">DESIGN</tspan><tspan x="472" y="1330">THINKING</tspan></text>
    <text class="venn-light" font-size="17"><tspan x="606" y="1278">INTUITIVE</tspan><tspan x="606" y="1298">AND</tspan><tspan x="606" y="1318">CREATIVE</tspan><tspan x="606" y="1338">THINKING</tspan></text>
    <text class="axis-label-light"><tspan x="292" y="1402">Understand</tspan><tspan x="292" y="1425">Problem</tspan></text>
    <text class="axis-label-light"><tspan x="574" y="1407">Design</tspan><tspan x="574" y="1430">Solution</tspan></text>
    <path d="M463,1396 H500 V1390 L516,1402 L500,1414 V1408 H463 Z" fill="#fff" stroke="var(--outline)" stroke-width="2.5"/>
    <path d="M490,1413 H453 V1407 L437,1420 L453,1432 V1426 H490 Z" fill="#fff" stroke="var(--outline)" stroke-width="2.5"/>
  </g>

  <!-- Contribution Venn (warm) -->
  <g class="venn venn--warm">
    <ellipse cx="957" cy="1334" rx="131" ry="123" fill="url(#grad-amber)" stroke="var(--outline)" stroke-width="3"/>
    <ellipse cx="1122" cy="1335" rx="128" ry="123" fill="url(#grad-red)" stroke="var(--outline)" stroke-width="3"/>
    <ellipse cx="1122" cy="1335" rx="128" ry="123" fill="url(#grad-sky)" clip-path="url(#clip-oval-left-b)"/>
    <ellipse cx="957" cy="1334" rx="131" ry="123" fill="none" stroke="var(--outline)" stroke-width="1" stroke-dasharray="3 3"/>
    <text class="venn-light" font-size="12.5"><tspan x="910" y="1317">DESIGN THINKING IN</tspan><tspan x="910" y="1340">MANAGEMENT AND</tspan><tspan x="910" y="1364">BUSINESS STRATEGY</tspan></text>
    <text class="venn-light" font-size="12.5"><tspan x="1036" y="1333">CONTRIBUTION</tspan><tspan x="1036" y="1356">AREA</tspan></text>
    <text class="venn-light" font-size="12.5"><tspan x="1167" y="1330">RESEARCH THROUGH</tspan><tspan x="1167" y="1353">DESIGN - R&amp;D</tspan></text>
  </g>

  <!-- Reflection model (warm) -->
  <g class="reflection reflection--warm">
    <circle cx="1595" cy="1356" r="131" fill="url(#grad-red)" stroke="var(--outline)" stroke-width="3"/>
    <text class="reflect-head" font-size="16"><tspan x="1596" y="1308">REFLECTION INVOLVES</tspan><tspan x="1596" y="1327">THREE ELEMENTS:</tspan></text>
    <text class="reflect-list" font-size="16"><tspan x="1596" y="1366">RETURNING TO EXPERIENCE</tspan><tspan x="1596" y="1385">ATTENDING TO FEELINGS</tspan><tspan x="1596" y="1404">EVALUATING EXPERIENCE</tspan></text>
    <circle cx="1493" cy="1496" r="73" fill="url(#grad-pearl)" stroke="var(--outline)" stroke-width="3"/>
    <circle cx="1694" cy="1496" r="73" fill="url(#grad-pearl)" stroke="var(--outline)" stroke-width="3"/>
    <text class="reflect-node" font-size="16" fill="var(--deep-red)"><tspan x="1493" y="1497">REFLECTING</tspan><tspan x="1493" y="1516">ON ACTION</tspan></text>
    <text class="reflect-node" font-size="16" fill="var(--deep-red)"><tspan x="1694" y="1495">REFLECTING</tspan><tspan x="1694" y="1514">ON ACTION</tspan></text>
    <text class="reflect-caption" font-size="15"><tspan x="1609" y="1605">REFLECTION IS AN ACTIVE PROCESS OF</tspan><tspan x="1609" y="1624">WITNESSING ONE'S WON EXPERIENCE IN ORDER TO</tspan><tspan x="1609" y="1643">EXAMINE IT MORE CLOSELY, GIVE MEANING TO IT,</tspan><tspan x="1609" y="1662">AND LEARN FROM IT.</tspan></text>
  </g>
</svg>
</body>
</html>
```